A Medical Institute that offers treatment for the severely depressed

We need a WEB design for The Brightmoor Clinic based in south Florida. We offer a medical treatment that helps severely depressed people, This treatment is only available in a few places around the world. We want a classy design, that compliments our logo. The site will have the home page which will talk briefly about ketamine treatments and our center, a page describing ketamine for the treatment of depression, a page describing the treatment in detail, an about us page, and a FAQ page. The people looking at this site are in a lot of distress, or have a family member who is, and they are looking for hope that they will be able to lead a normal life with this treatment. They have tried everything else out there and nothing has helped, they are desperate for an alternative.

Target Market(s)

People suffering from depression that are researching treatment options on the WEB and specifically ketamine treatments

Industry/Entity Type

Medical

Number of Pages Required

5+ page

Requirements
Must have
• I am not set on any particular design or content. While I personally love color, I don't see it for this project given the attached logo.
Should not have
• sound, a lot of flash, I don't want the site to be difficult to load. I do not want to see the old design of a bar down the side and a graphic across the top, I can do that myself.

```html
<!DOCTYPE html>
<html lang="en">
<head>
<meta charset="utf-8">
<title>The Brightmoor Clinic</title>
<link href="https://fonts.googleapis.com/css2?family=Roboto:ital,wght@0,300;0,400;0,500;1,400&display=swap" rel="stylesheet">
<style>
:root{
  --header-top:#e3a64a;
  --header-bottom:#d89b3f;
  --nav-active:#e8c43c;
  --phone:#fff36b;
  --heading:#7a5a1c;
  --text:#444;
  --text-dark:#222;
  --rule:#d6d6d6;
  --panel:#f2f2f2;
  --panel-border:#d9d9d9;
  --button-top:#c58f34;
  --button-bottom:#a8741f;
  --footer:#e8c444;
  --social:#1f6fb5;
  --gold:#c48a3a;
}
*{margin:0;padding:0;box-sizing:border-box}
html,body{width:1073px;height:1200px;overflow:hidden;background:#fff;font-family:'Roboto',sans-serif;color:var(--text)}
.page{position:relative;width:1073px;height:1200px}

.site-header{position:absolute;left:0;top:0;width:1073px;height:106px;background:linear-gradient(var(--header-top) 0,var(--header-top) 60%,var(--header-bottom) 100%)}
.logo{position:absolute;left:67px;top:24px;width:187px;height:69px;background:#fbf3b8;border:1px solid #333;display:flex;align-items:center;justify-content:center;text-align:center;font-size:19px;font-weight:500;line-height:1.1;color:#222}
.call{position:absolute;right:66px;top:20px;display:flex;align-items:center;gap:6px;font-size:12.5px;color:#222}
.call svg{width:16px;height:16px}
.call .number{font-size:20px;font-weight:300;color:var(--phone)}
.main-nav{position:absolute;right:66px;top:64px;display:flex;gap:0}
.main-nav a{display:block;height:29px;line-height:29px;padding:0 18px;font-size:12.4px;color:#fff;text-decoration:none}
.main-nav a:last-child{padding-right:0}
.main-nav a.active{background:var(--nav-active);color:var(--text-dark)}

.hero{position:absolute;left:67px;top:116px;width:940px;height:336px;background:linear-gradient(110deg,#fff 55%,#fdf4c4 80%,#fbe69a 100%);overflow:hidden}
.hero svg.photo{position:absolute;left:0;top:0}
.quote{position:absolute;left:578px;top:112px;width:340px;text-align:center;font-style:italic;font-size:18px;line-height:25px;color:var(--text-dark)}
.dots{position:absolute;left:716px;top:305px;display:flex;gap:8px}
.dots span{width:11px;height:11px;border-radius:50%;background:#222}
.dots span.on{background:var(--gold)}

.content{position:absolute;left:67px;top:0;width:618px}
.block{position:absolute;left:0;width:618px}
.block h2{font-size:19.8px;font-weight:400;color:var(--heading);margin-left:-1px;letter-spacing:.2px}
.block h3{font-size:16.5px;font-weight:400;color:var(--text-dark);margin-top:10px}
.block p{font-size:11.9px;font-weight:300;line-height:19.8px;color:var(--text);margin-top:6px}
.block .cta{font-size:15.6px;font-style:italic;font-weight:400;color:var(--text-dark);margin-top:20px}
.rule{position:absolute;left:0;width:618px;height:1px;background:var(--rule)}

.contact-panel{position:absolute;left:710px;top:475px;width:297px;height:366px;background:var(--panel);border:1px solid var(--panel-border)}
.contact-panel h2{position:absolute;left:18px;top:21px;font-size:19px;font-weight:400;color:var(--heading)}
.field{position:absolute;left:18px;width:258px;height:34px;background:#fff;border:1px solid #ccc;font-size:10.5px;color:#666;padding:10px 12px}
.field.message{height:106px}
.submit{position:absolute;left:162px;top:310px;width:113px;height:35px;background:linear-gradient(var(--button-top),var(--button-bottom));color:#fff;font-size:12px;font-weight:500;letter-spacing:.3px;display:flex;align-items:center;justify-content:center}

.site-footer{position:absolute;left:0;top:1090px;width:1073px;height:110px;background:var(--footer)}
.footer-nav{position:absolute;left:67px;top:30px;display:flex;gap:29px}
.footer-nav a{font-size:9.9px;font-weight:500;color:var(--text-dark);text-decoration:none}
.copyright{position:absolute;left:67px;top:66px;font-size:9.9px;color:#5a4a1a}
.connect{position:absolute;right:66px;top:42px;display:flex;align-items:center;gap:4px;font-size:12px;color:var(--text-dark)}
.connect .label{margin-right:6px}
.connect .social{width:27px;height:27px;border-radius:50%;background:var(--social)}
</style>
</head>
<body>
<div class="page">

  <header class="site-header">
    <div class="logo">The Brightmoor<br>Clinic</div>
    <div class="call">
      <svg viewBox="0 0 16 16" aria-hidden="true"><rect width="16" height="16" rx="2" fill="#fff"/><path d="M5 3.5c-1 .6-1.4 1.6-1 3 .7 2.5 2.5 4.8 5 6 1.2.5 2.2.2 2.8-.7l-1.8-1.7-1.2.7c-1.2-.7-2-1.8-2.4-3l1-.9L6.4 4z" fill="#d89b3f"/></svg>
      <span>CALL US TODAY:</span><span class="number">123-456-7890</span>
    </div>
    <nav class="main-nav">
      <a class="active" href="#">HOME</a>
      <a href="#">KETAMINE DESCRIPTION</a>
      <a href="#">ABOUT US</a>
      <a href="#">THE KETAMINE THERAPY</a>
      <a href="#">FAQ</a>
      <a href="#">CONTACT US</a>
    </nav>
  </header>

  <section class="hero">
    <svg class="photo" width="940" height="336" viewBox="0 0 940 336">
      <defs>
        <linearGradient id="photoTone" x1="0" y1="0" x2="1" y2="1">
          <stop offset="0" stop-color="#b89a3c"/>
          <stop offset=".45" stop-color="#8a7a45"/>
          <stop offset="1" stop-color="#7d7a72"/>
        </linearGradient>
      </defs>
      <path d="M0 0H507Q640 150 470 336H0Z" fill="none" stroke="var(--gold)" stroke-width="10"/>
      <path role="img" aria-label="Photo of a smiling man in glasses outdoors" d="M0 0H503Q630 150 466 336H0Z" fill="url(#photoTone)"/>
    </svg>
    <p class="quote">“ After suffering with depression for 17 years, I finally feel normal again” say Daniel, after receiving just one ketamine treatment...</p>
    <div class="dots"><span class="on"></span><span></span><span></span><span></span></div>
  </section>

  <main class="content">
    <section class="block" style="top:472px">
      <h2>KETAMINE TREATMENTS FOR DEPRESSION</h2>
      <p>Are you or someone you love suffering from depression?&nbsp; Have you had thoughts of suicide?&nbsp; Have you tried medications&nbsp; and nothing is working?&nbsp; Do you feel&nbsp; hopeless?&nbsp; A new treatment offers hope for those people who are suffering from depression and are desperate to get their life back.&nbsp; Ketamine has been used for years as a drug for anesthesia, but administered in small doses, it is extremely effective in treating patients with depression.</p>
      <p class="cta">Call us today to find out if ketamine therapy is right for you.</p>
    </section>
    <div class="rule" style="top:649px"></div>

    <section class="block" style="top:669px">
      <h2>KETAMINE DESCRIPTION</h2>
      <h3>From Club Drug to Wonder Drug</h3>
      <p>When it comes to profound depression, many people just can't get relief from current treatments.<br>Now there's more evidence that the anesthetic ketamine, sometimes abused as a club drug, has potential as a fast-acting treatment for the condition. Ketamine is an FDA-approved anesthetic which has been used in humans for over 50 years.&nbsp; In low doses, Ketamine has shown very positive promise in providing rapid relief of depression, along with helping the depressed phase of bipolar disorder, anxiety and post-traumatic stress disorder(PTSD), with very few side effects.</p>
    </section>
    <div class="rule" style="top:873px"></div>

    <section class="block" style="top:893px">
      <h2>THE KETAMINE THERAPY</h2>
      <h3>What is Involved with Ketamine Therapy?</h3>
      <p>Ketamine can be delivered to the patient in 3 different ways: IV infusion, intra-muscular shot or a nasal spray. Several studies have shown that the most effective option is the IV infused over 45 minutes.&nbsp; The nasal spray is used in between treatments to help maintain the therapy but does not deliver the impact that the other two options provide. Some patients don't notice much difference between the shot and the IV, some patients get longer lasting relief with the IV.&nbsp; Every patient is different and the therapy is tailored to meet your needs.</p>
    </section>
  </main>

  <aside class="contact-panel">
    <h2>CONTACT US TODAY</h2>
    <div class="field" style="top:59px">Name</div>
    <div class="field" style="top:102px">Email Address</div>
    <div class="field" style="top:145px">Phone No.</div>
    <div class="field message" style="top:187px">Message</div>
    <div class="submit">SUBMIT NOW</div>
  </aside>

  <footer class="site-footer">
    <nav class="footer-nav">
      <a href="#">HOME</a>
      <a href="#">KETAMINE DESCRIPTION</a>
      <a href="#">ABOUT US</a>
      <a href="#">THE KETAMINE THERAPY</a>
      <a href="#">FAQ</a>
      <a href="#">CONTACT US</a>
    </nav>
    <p class="copyright">Copyright ©2015.CompanyName.All Right Reserved.| Term of Services</p>
    <div class="connect">
      <span class="label">CONNECT US:</span>
      <span class="social" role="img" aria-label="Social profile link"></span>
      <span class="social" role="img" aria-label="Social profile link"></span>
      <span class="social" role="img" aria-label="Social profile link"></span>
    </div>
  </footer>

</div>
</body>
</html>
```